Magazine Cover & Back, Course Overview

Please read this whole description and follow directions before proceeding. Please do not submit multiple designs that look similar. If you submit multiple designs that look similar you will be disqualified and receive a poor rating. A magazine design includes a cover and back. This is a single design and should be submitted as such. Do not submit one design for the front only, then a separate design for the back, then a third mock up. Submit all as a single design. I need a magazine cover and back. The size will be standard paper size, 8-1/2" x 11". It will be used for a course overview, a summary of a boating instruction course. I have attached examples and pictures that can be used. I have also attached required content. The final designs must NOT be AI files. Text must be editable with Adobe Acrobat DC.

Target Market(s)

Military & Government

Industry/Entity Type

Military & Government

Requirements
Must have
• See attached.
Nice to have
• See attached.
Should not have
• See attached.

```html
<!DOCTYPE html>
<html lang="en">
<head>
<meta charset="utf-8">
<title>Diver Support Vessel Training – Course Overview Cover &amp; Back</title>
<link href="https://fonts.googleapis.com/css2?family=Poppins:wght@500;600;700;800&family=Oswald:wght@500&display=swap" rel="stylesheet">
<style>
  :root{
    --page-bg:#eeeeee;
    --navy-deep:#1a3a68;
    --navy:#1f4a86;
    --sky:#2e78d8;
    --sky-light:#4f94e4;
    --shore:#1b2f4d;
    --gold:#f5b50c;
    --white:#ffffff;
    --body-font:'Poppins', sans-serif;
    --condensed-font:'Oswald', sans-serif;
  }
  *{margin:0;padding:0;box-sizing:border-box;}
  html,body{width:852px;height:1200px;overflow:hidden;background:var(--page-bg);}
  body{position:relative;font-family:var(--body-font);color:var(--white);}

  .spread{
    position:absolute;left:26px;top:290px;width:800px;height:620px;overflow:hidden;
    box-shadow:0 6px 16px rgba(0,0,0,.35);
  }
  .spread-scene{
    position:absolute;inset:0;
    background:
      linear-gradient(180deg,
        rgba(23,58,108,0) 0%,
        rgba(23,58,108,0) 54%,
        rgba(27,47,77,.55) 59%,
        rgba(27,47,77,.45) 62%,
        rgba(30,68,120,.35) 66%,
        rgba(23,58,108,.55) 100%),
      linear-gradient(90deg, var(--navy) 0%, var(--navy) 50%, var(--sky) 80%, var(--sky-light) 100%);
  }

  /* back cover */
  .back{position:absolute;left:0;top:0;width:400px;height:620px;}
  .badge{
    position:absolute;left:32px;top:42px;width:62px;height:62px;border-radius:50%;
    background:var(--white);border:3px solid var(--gold);
  }
  .course-for{position:absolute;left:107px;top:34px;font-size:18px;font-weight:700;line-height:1.2;}
  .feature-col{position:absolute;top:68px;font-size:9px;font-weight:600;line-height:1.15;text-transform:uppercase;}
  .feature-col .hl{color:var(--gold);font-weight:700;display:block;}

  .brand{position:absolute;}
  .brand-row{display:flex;align-items:center;gap:8px;}
  .brand-dot{width:22px;height:22px;border-radius:50%;border:1.5px solid var(--white);flex:none;}
  .brand-name{font-size:21px;font-weight:600;line-height:1;}
  .brand-sub{font-size:8.5px;font-weight:600;letter-spacing:1.5px;text-transform:uppercase;margin:4px 0 0 30px;}
  .brand-back{left:117px;top:228px;}
  .brand-front{left:123px;top:540px;}

  .overview-frame{position:absolute;left:120px;top:402px;width:149px;height:26px;}
  .overview-title{position:absolute;left:120px;top:402px;width:149px;height:26px;line-height:26px;text-align:center;font-size:8.5px;font-weight:600;}
  .web{position:absolute;left:110px;top:437px;width:168px;text-align:center;font-size:7.5px;font-weight:600;line-height:1.2;}
  .web span{color:var(--gold);}
  .photo-circle{position:absolute;top:468px;width:102px;height:102px;border-radius:50%;border:3px solid var(--gold);}
  .pc-helm{left:39px;background:radial-gradient(circle at 45% 40%,#8a8e93,#3a3e44);}
  .pc-deck{left:146px;background:linear-gradient(180deg,#6fa3d8 0%,#b9c3cc 45%,#707a84 100%);}
  .pc-ladder{left:254px;background:linear-gradient(90deg,#2b2e33 0%,#9aa6b1 60%,#d3d9de 100%);}

  /* front cover */
  .front{position:absolute;left:400px;top:0;width:400px;height:620px;}
  .title-line{position:absolute;right:34px;font-weight:800;line-height:1;white-space:nowrap;}
  .title-top{top:28px;font-size:41px;}
  .title-main{top:58px;font-size:94px;color:var(--gold);letter-spacing:-1.5px;}
  .title-sub{top:139px;font-size:27px;font-weight:700;}

  .pitch{position:absolute;line-height:1.2;white-space:nowrap;}
  .pitch-label{font-size:10.5px;font-weight:700;}
  .pitch-hl{font-family:var(--condensed-font);font-weight:500;color:var(--gold);font-size:17px;line-height:1;letter-spacing:-.4px;}
  .left{left:33px;}
  .right{right:34px;text-align:right;}

  .vessel-photo{
    position:absolute;left:64px;top:255px;width:290px;height:270px;border-radius:6px;
    background:
      linear-gradient(180deg, rgba(46,120,216,0) 0%, rgba(46,120,216,0) 38%, #c9d0d8 52%, #e6e9ec 66%, #aab3bd 82%, #5d6d82 92%, rgba(31,74,134,0) 100%);
    -webkit-mask-image:linear-gradient(90deg,transparent 0%,#000 12%,#000 88%,transparent 100%);
            mask-image:linear-gradient(90deg,transparent 0%,#000 12%,#000 88%,transparent 100%);
  }
</style>
</head>
<body>
  <main class="spread">
    <div class="spread-scene" role="img" aria-label="Photograph of open water under a blue sky with a wooded shoreline, spanning back and front cover"></div>

    <section class="back">
      <div class="badge" role="img" aria-label="Partner badge"></div>
      <h2 class="course-for">Custom Made Course for</h2>
      <p class="feature-col" style="left:107px;"><span class="hl">Scenarios and<br>vessels based</span>on OIC involvement</p>
      <p class="feature-col" style="left:226px;"><span class="hl">Specific</span>users</p>
      <p class="feature-col" style="left:283px;"><span class="hl">Client feedback<br>&amp; after action</span>reviews</p>

      <div class="brand brand-back">
        <div class="brand-row"><span class="brand-dot"></span><span class="brand-name">Harbor Reach</span></div>
        <div class="brand-sub">Marine Services, LLC</div>
      </div>

      <svg class="overview-frame" viewBox="0 0 149 26" aria-hidden="true">
        <path d="M1.5 18 V1.5 H17" fill="none" stroke="#f5b50c" stroke-width="3"/>
        <path d="M132 24.5 H147.5 V8" fill="none" stroke="#f5b50c" stroke-width="3"/>
      </svg>
      <div class="overview-title">COURSE OVERVIEW</div>
      <p class="web">www.<span>harborreachmarine</span>.com</p>

      <div class="photo-circle pc-helm" role="img" aria-label="Photo of a vessel helm console with wheel and controls"></div>
      <div class="photo-circle pc-deck" role="img" aria-label="Photo of a sailor at work on deck"></div>
      <div class="photo-circle pc-ladder" role="img" aria-label="Photo of a sailor climbing a ladder on the vessel"></div>
    </section>

    <section class="front">
      <h1>
        <span class="title-line title-top">DIVER SUPPORT</span>
        <span class="title-line title-main">VESSEL</span>
        <span class="title-line title-sub">TRAINING</span>
      </h1>

      <div class="vessel-photo" role="img" aria-label="Photo of a white diver support vessel underway flying a national flag"></div>

      <p class="pitch pitch-label left" style="top:206px;">To assist Navy Sailors<br>with Becoming More</p>
      <p class="pitch pitch-hl left" style="top:234px;">PROFICIENT COXSWAINS</p>
      <p class="pitch pitch-label left" style="top:265px;">Taught by Reputable</p>
      <p class="pitch pitch-hl left" style="top:279px;">USCG LICENSED</p>
      <p class="pitch pitch-label left" style="top:297px;">Boat Captains</p>

      <p class="pitch pitch-label right" style="top:206px;">Focused on Safety &amp;</p>
      <p class="pitch pitch-hl right" style="top:221px;">CLOSE-QUARTERS</p>
      <p class="pitch pitch-hl right" style="top:240px;">MANEUVERING</p>
      <p class="pitch pitch-label right" style="top:265px;">Includes Useful</p>
      <p class="pitch pitch-hl right" style="top:279px;">AIDS</p>

      <div class="brand brand-front">
        <div class="brand-row"><span class="brand-dot"></span><span class="brand-name">Harbor Reach</span></div>
        <div class="brand-sub">Marine Services, LLC</div>
      </div>
    </section>
  </main>
</body>
</html>
```